The most modern business card ever !!!

Our company call “Vantilo”. Vantilo is a technology company specialized in cruises solutions. Out main product is a platform to reserve cruises. This is a revolutionary platform that make easier to travel agencies and final users to reserve cruises across dozen companies like tarvik, welbi, dpv, hbt, etc..We are a “start up”, with a young team of developers and we want to transmit it.. For it, we want something different, a modern business card that represent cruises and technology.. When someone receive this card, this person should say: wowww this is different… this is modern… this is a cruise related company..
Contact Information for Business Card
Requirements
Must have
- diferent, modern
Should not have
- traditions business card

```html
<!DOCTYPE html>
<html lang="en">
<head>
<meta charset="UTF-8">
<title>Vantilo Business Card</title>
<link href="https://fonts.googleapis.com/css2?family=Montserrat:wght@400;500;600;800&display=swap" rel="stylesheet">
<style>
  :root {
    --backdrop: #2a2b2f;
    --paper: #ffffff;
    --ink: #0a0a0a;
    --accent: #2ea3dc;
    --photo-light: #c9cdd2;
    --photo-dark: #6f6258;
  }
  * { box-sizing: border-box; margin: 0; padding: 0; }
  html, body {
    width: 1200px; height: 900px; overflow: hidden;
    background: var(--backdrop);
    font-family: "Montserrat", Arial, sans-serif;
  }
  .card {
    position: absolute;
    width: 520px; height: 300px;
    background: var(--paper);
    overflow: hidden;
    box-shadow: 0 14px 30px rgba(0,0,0,.45);
  }
  .card--front { left: 60px; top: 300px; }
  .card--back { left: 620px; top: 300px; }
  .card__shapes { position: absolute; inset: 0; width: 100%; height: 100%; }

  .brand { position: absolute; left: 92px; top: 66px; }
  .brand__name {
    font-size: 52px; font-weight: 600; color: var(--ink);
    letter-spacing: 1px; line-height: 1;
  }
  .brand__url {
    margin-top: 4px; padding-left: 36px;
    font-size: 16px; font-weight: 600; color: var(--ink); letter-spacing: .5px;
  }
  .brand__url span { color: var(--accent); }

  .portrait {
    position: absolute; left: 58px; top: 40px;
    width: 140px; height: 140px; border-radius: 50%;
    border: 4px solid var(--accent);
    padding: 5px; background: var(--paper);
  }
  .portrait__fill {
    width: 100%; height: 100%; border-radius: 50%;
    background: linear-gradient(160deg, var(--photo-light), var(--photo-dark));
  }
  .identity { position: absolute; left: 0; width: 256px; top: 206px; text-align: center; }
  .identity__name { font-size: 27px; font-weight: 800; color: var(--ink); letter-spacing: .5px; }
  .identity__role { font-size: 17px; font-weight: 500; color: var(--accent); letter-spacing: .5px; margin-top: 2px; }

  .contacts { position: absolute; left: 320px; top: 78px; list-style: none; }
  .contacts__item {
    display: flex; align-items: center; gap: 12px;
    color: var(--paper); font-size: 13px; font-weight: 500;
    margin-bottom: 14px; line-height: 1.35;
  }
  .contacts__icon {
    flex: none; width: 30px; height: 30px; border-radius: 50%;
    background: var(--accent);
    display: flex; align-items: center; justify-content: center;
  }
  .contacts__icon svg { width: 16px; height: 16px; }
</style>
</head>
<body>

<section class="card card--front">
  <svg class="card__shapes" viewBox="0 0 520 300" aria-hidden="true">
    <polygon points="0,212 520,168 520,214 0,258" fill="var(--ink)"/>
    <polygon points="0,182 330,158 318,186 0,212" fill="var(--accent)"/>
    <polygon points="400,0 442,0 300,236 268,236" fill="var(--accent)"/>
  </svg>
  <div class="brand">
    <div class="brand__name">Vantilo</div>
    <div class="brand__url">www.<span>vantilo</span>.com</div>
  </div>
</section>

<section class="card card--back">
  <svg class="card__shapes" viewBox="0 0 520 300" aria-hidden="true">
    <polygon points="248,0 520,0 520,300 288,300" fill="var(--ink)"/>
    <polygon points="262,30 284,14 300,190 520,222 520,250 288,214" fill="var(--accent)"/>
  </svg>
  <div class="portrait">
    <div class="portrait__fill" role="img" aria-label="Portrait photo of Dario Menes"></div>
  </div>
  <div class="identity">
    <div class="identity__name">DARIO MENES</div>
    <div class="identity__role">FOUNDER &amp; CEO</div>
  </div>
  <ul class="contacts">
    <li class="contacts__item">
      <span class="contacts__icon">
        <svg viewBox="0 0 16 16" fill="none" stroke="#0a0a0a" stroke-width="1.4"><rect x="2" y="4" width="12" height="8"/><polyline points="2,4 8,9 14,4"/></svg>
      </span>
      d.menes@vantilo.com
    </li>
    <li class="contacts__item">
      <span class="contacts__icon">
        <svg viewBox="0 0 16 16" fill="#0a0a0a"><path d="M4 2l2.5 3-1.3 1.3a8 8 0 0 0 4.5 4.5L11 9.5l3 2.5-1.5 2C7.5 14 2 8.5 2 3.5z"/></svg>
      </span>
      <span>+4412078830<br>+4412078830</span>
    </li>
    <li class="contacts__item">
      <span class="contacts__icon">
        <svg viewBox="0 0 16 16" fill="none" stroke="#0a0a0a" stroke-width="1.3"><circle cx="8" cy="8" r="6"/><ellipse cx="8" cy="8" rx="2.6" ry="6"/><line x1="2" y1="8" x2="14" y2="8"/></svg>
      </span>
      www.vantilo.com
    </li>
  </ul>
</section>

</body>
</html>
```